Business Card Design for new logo

Business card Design for new logo. Follow colors from logo.
The company has offices in multiple comtries
Want to have some bulltes on the countries and also on the main services

Something like
USA*Dominican Republic*LATAM

Consulting*Healthcare IT*Tranformation

Industry/Entity Type

Information Technology

Contact Information for Business Card

Address, Phones, countries, name and position

Miron castell

Founder and CEO

947 Quarry Ln
Mill haven, PA 16835

Mcastell@novelquin.com

www.novelquin.com

717-352-6081

828-444-4444

```html
<!DOCTYPE html>
<html lang="en">
<head>
<meta charset="utf-8">
<title>Novelquin Business Card</title>
<link href="https://fonts.googleapis.com/css2?family=Roboto:wght@400;500;700&display=swap" rel="stylesheet">
<style>
  :root {
    --blue: #2574b5;
    --orange: #f58b4c;
    --paper: #f3f3f3;
    --ink: #4a4a4a;
    --rule: #c9c9c9;
    --backdrop: #e6e4e0;
    --white: #ffffff;
  }
  * { margin: 0; padding: 0; box-sizing: border-box; }
  html, body {
    width: 1125px; height: 1200px; overflow: hidden;
    background: var(--backdrop);
    font-family: "Roboto", Arial, sans-serif;
  }
  .card {
    position: absolute; left: 162px; width: 800px; height: 457px;
    box-shadow: 0 4px 12px rgba(0,0,0,0.18);
    overflow: hidden;
  }
  .card-front { top: 105px; background: var(--paper); }
  .card-back { top: 620px; background: var(--blue); }

  .brand {
    position: absolute; display: flex; align-items: center; gap: 12px;
    font-weight: 500; white-space: nowrap;
  }
  .brand-dot { width: 22px; height: 22px; border-radius: 50%; background: var(--orange); }
  .card-front .brand { left: 88px; top: 260px; transform: translateY(-50%); color: var(--blue); font-size: 44px; }
  .card-back .brand { left: 50%; top: 210px; transform: translate(-50%, -50%); color: var(--white); font-size: 56px; }

  .divider {
    position: absolute; left: 423px; top: 110px; width: 1px; height: 245px; background: var(--rule);
  }
  .contact { position: absolute; left: 460px; top: 108px; color: var(--ink); }
  .contact-name { color: var(--blue); font-size: 29px; font-weight: 700; letter-spacing: 0.3px; line-height: 1; text-transform: uppercase; }
  .contact-role { color: var(--orange); font-size: 19px; font-weight: 500; margin-top: 6px; text-transform: uppercase; }
  .contact-address { font-size: 19px; line-height: 25px; margin-top: 16px; }
  .contact-list { list-style: none; margin-top: 13px; font-size: 19px; }
  .contact-list li { display: flex; align-items: center; gap: 10px; height: 25.5px; }
  .contact-list svg { width: 18px; height: 18px; fill: var(--blue); flex: none; }

  .stripe { position: absolute; left: 0; bottom: 0; width: 800px; height: 20px; }

  .tagline {
    position: absolute; left: 0; right: 0; top: 368px; text-align: center;
    color: var(--white); font-size: 19px; line-height: 25px;
  }
</style>
</head>
<body>
  <section class="card card-front">
    <div class="brand"><span class="brand-dot"></span>Novelquin</div>
    <div class="divider"></div>
    <div class="contact">
      <h1 class="contact-name">Miron Castell</h1>
      <p class="contact-role">Founder &amp; CEO</p>
      <p class="contact-address">947 Quarry Ln<br>Mill haven, PA 16835</p>
      <ul class="contact-list">
        <li><svg viewBox="0 0 24 24"><path d="M6.6 10.8a15.1 15.1 0 0 0 6.6 6.6l2.2-2.2a1 1 0 0 1 1-.25 11.4 11.4 0 0 0 3.6.57 1 1 0 0 1 1 1V20a1 1 0 0 1-1 1A17 17 0 0 1 3 4a1 1 0 0 1 1-1h3.5a1 1 0 0 1 1 1c0 1.25.2 2.45.57 3.57a1 1 0 0 1-.25 1z"/></svg>717-352-6081</li>
        <li><svg viewBox="0 0 24 24"><path d="M7 1h10a2 2 0 0 1 2 2v18a2 2 0 0 1-2 2H7a2 2 0 0 1-2-2V3a2 2 0 0 1 2-2zm0 3v14h10V4zm5 15.2a1.1 1.1 0 1 0 0 2.2 1.1 1.1 0 0 0 0-2.2z"/></svg>828-444-4444</li>
        <li><svg viewBox="0 0 24 24"><path d="M3 6h18v12H3zm1.5 1.5v.3L12 13l7.5-5.2v-.3zm0 2.1V16.5h15V9.6L12 14.8z"/></svg>Mcastell@novelquin.com</li>
        <li><svg viewBox="0 0 24 24"><path d="M12 2a10 10 0 1 0 0 20 10 10 0 0 0 0-20zm-1 17.9A8 8 0 0 1 4.2 10L9 14.8v1a2 2 0 0 0 2 2zm6.9-2.5A2 2 0 0 0 16 16h-1v-3a1 1 0 0 0-1-1H8v-2h2a1 1 0 0 0 1-1V7h2a2 2 0 0 0 2-2v-.4a8 8 0 0 1 2.9 12.8z"/></svg>www.novelquin.com</li>
      </ul>
    </div>
    <svg class="stripe" viewBox="0 0 800 20" aria-hidden="true">
      <polygon points="0,0 525,0 518,20 0,20" fill="var(--blue)"/>
      <polygon points="530,0 800,0 800,20 523,20" fill="var(--orange)"/>
    </svg>
  </section>

  <section class="card card-back">
    <div class="brand"><span class="brand-dot"></span>Novelquin</div>
    <p class="tagline">USA.Dominican Republic.LATAM<br>Consulting.Healthcare IT.Tranformation</p>
  </section>
</body>
</html>
```